Business / Stationery Design Project

Hi,

I need business cards and all other stationary designed for my new finance broking business.

Stationary required:

Business card
Letter head
with compliments
envelopes

There is gold in the logo design so some gold would be good and open to other creative ideas / colours.

Regards
Milo
Updates

Target Market(s)

Small to medium business customers. Also to appeal to referrers who include accounting firms and other associated professionals (valuers etc)

Industry/Entity Type

Finance

Requirements
Must have
• Professional, classy look.

```html
<!DOCTYPE html>
<html lang="en">
<head>
<meta charset="utf-8">
<title>Halden Finance – Business Card</title>
<link rel="stylesheet" href="https://fonts.googleapis.com/css2?family=Open+Sans:wght@400;600&display=swap">
<style>
  :root {
    --backdrop: #5a5a5c;
    --card: #ffffff;
    --ink: #1d1d1b;
    --gold: #c9a15c;
    --tone-light: #f3e6d3;
    --tone-mid: #d9bb8f;
    --tone-deep: #9a6a3f;
  }
  html, body {
    margin: 0;
    padding: 0;
    width: 1200px;
    height: 1023px;
    overflow: hidden;
    background: var(--backdrop);
    font-family: "Open Sans", Arial, sans-serif;
  }
  .canvas {
    position: relative;
    width: 1200px;
    height: 1023px;
  }
  .card {
    position: absolute;
    left: 220px;
    width: 760px;
    height: 434px;
    background: var(--card);
    overflow: hidden;
    box-shadow: 0 8px 24px rgba(0,0,0,0.35);
  }
  .card--front { top: 50px; }
  .card--back  { top: 539px; }

  .card__decor {
    position: absolute;
    inset: 0;
  }
  .card--front .card__decor {
    background: linear-gradient(to top right,
      var(--tone-deep) 0%, var(--tone-mid) 22%, var(--tone-light) 40%, var(--card) 58%);
  }
  .card--back .card__decor {
    background: linear-gradient(to bottom left,
      var(--tone-deep) 0%, var(--tone-mid) 22%, var(--tone-light) 40%, var(--card) 58%);
  }

  .brand {
    position: absolute;
    display: flex;
    align-items: center;
    color: var(--ink);
    font-weight: 600;
    letter-spacing: 0.06em;
    text-transform: uppercase;
    white-space: nowrap;
  }
  .brand__dot {
    border-radius: 50%;
    background: var(--gold);
    flex: none;
  }
  .card--front .brand {
    left: 250px;
    top: 110px;
    font-size: 44px;
    gap: 18px;
  }
  .card--front .brand__dot { width: 26px; height: 26px; }

  .card--back .brand {
    left: 50px;
    top: 58px;
    font-size: 22px;
    gap: 10px;
  }
  .card--back .brand__dot { width: 13px; height: 13px; }

  .contact {
    position: absolute;
    left: 90px;
    top: 185px;
    color: var(--ink);
    font-size: 14px;
    line-height: 1.45;
  }
  .contact__name {
    margin: 0;
    color: var(--gold);
    font-size: 17px;
    text-transform: uppercase;
    letter-spacing: 0.02em;
  }
  .contact__role {
    margin: 0 0 36px;
    font-size: 13px;
  }
  .contact__list {
    margin: 0;
    padding: 0;
    list-style: none;
  }
  .contact__label { color: var(--gold); }
</style>
</head>
<body>
<main class="canvas">

  <section class="card card--front" aria-label="Business card front">
    <div class="card__decor" role="img" aria-label="Decorative sweep of layered gold and brown curved bands"></div>
    <div class="brand"><span class="brand__dot"></span>Halden Finance</div>
  </section>

  <section class="card card--back" aria-label="Business card back">
    <div class="card__decor" role="img" aria-label="Decorative sweep of layered gold and brown curved bands"></div>
    <div class="brand"><span class="brand__dot"></span>Halden Finance</div>
    <div class="contact">
      <p class="contact__name">Halden Finance</p>
      <p class="contact__role">Position</p>
      <ul class="contact__list">
        <li><span class="contact__label">tel:</span> 0116 496 0100</li>
        <li><span class="contact__label">fax:</span> 0116 496 0200</li>
        <li><span class="contact__label">email:</span> info@haldenfinance.co.uk</li>
        <li><span class="contact__label">web:</span> www.haldenfinance.co.uk</li>
      </ul>
    </div>
  </section>

</main>
</body>
</html>
```